依頼詳細
①TOPページのデザイン案をご提案ください。
②採用させていただく可能性の高い方と、
下層ページ1ページ、採用サイト等別サイト2ページ分について
ご相談したいと考えております。

<サイト概要>
・4ページ分(トップページ、下層ページ、採用サイト等2サイト)
・レスポンシブ
・セミナー案内などを、wordpressで更新していきます。

<納品物>
デザインカンプ(PSD希望ですが、AIでも可)を納品してください。

<応募条件>
・継続依頼も検討しているため、連絡がスムーズな方。

<参考サイト>
・株式会社ペネムス・ヤカルト
http://www.pnm-example.co.jp/

上記サイトのように、ファーストビューに背景に動画をフルスクリーンで表示させるのを希望しています。

・ツクリエ採用サイト
https://www.tsukurie-example.jp/saiyou/service/business.html

<提供する素材>
・写真、ロゴ、サイト内で使用するテキスト
サイトURL
http://www.meadowpath-x.com/
ページ数
4ページ
希望イメージ
シンプル 複雑
単色 カラフル
暗い 明るい
日常 高級
遊び心 厳粛
未来的 伝統的
女性的 男性的
希望する色
設定なし
納品ファイル
• イラストレーター形式 (.ai)
• フォトショップ形式 (.psd)
補足説明
・イラストレーター、フォトショップ、どちらで作成していただいても構いません。最終的に、制作データ(ai or psd)で納品をしていただける方。
・クライアント企業とのコミュニケーションに慣れていて、細かい修正等に対応していただける方
提供する素材を添付させていただきますので、
こちらをご使用ください。

<提供する素材>
・写真、ロゴ、サイト内で使用するテキスト
募集の締め切りを延長しましたので、
引き続きご提案をお待ちしております。
■ 選んだ理由

私たちのイメージに一番近いデザインを出していただきました。
またこちらの意向を汲んでくださり、
今後も引き続きお願いしたいと感じましたので決めさせていただきました。

■ 提案者全員のお礼・コメント

皆様、数々のご提案をいただき、ありがとうございました。

```html
<!DOCTYPE html>
<html lang="ja">
<head>
<meta charset="utf-8">
<title>株式会社メドウパス</title>
<link href="https://fonts.googleapis.com/css2?family=Noto+Sans+JP:wght@400;500;700&family=Noto+Serif+JP:wght@700&family=Libre+Baskerville:ital,wght@1,700&display=swap" rel="stylesheet">
<style>
:root{
  --navy:#1d3557;
  --navy-deep:#142640;
  --teal:#2fa7b7;
  --teal-light:#bfe6ea;
  --blue:#2b5f9e;
  --red:#e0322f;
  --ink:#333a44;
  --muted:#7a8593;
  --paper:#ffffff;
  --mist:#eef3f7;
}
*{box-sizing:border-box;margin:0;padding:0}
html,body{width:1200px;height:5400px;overflow:hidden}
body{font-family:"Noto Sans JP",sans-serif;color:var(--ink);background:var(--paper);position:relative;font-size:15px;line-height:1.8}
.block{position:absolute;left:0;width:1200px}
.ph{position:absolute}
/* section heading */
.sec-head{position:absolute;left:0;width:1200px;height:54px;display:flex;align-items:center;justify-content:center;gap:12px;
  background:linear-gradient(90deg,rgba(47,167,183,0) 0%,var(--teal) 30%,var(--teal) 70%,rgba(47,167,183,0) 100%)}
.sec-head .en{font-family:"Libre Baskerville",serif;font-style:italic;font-weight:700;font-size:30px;color:#fff}
.sec-head .ja{font-size:13px;color:#fff}
.btn{display:inline-block;background:var(--blue);color:#fff;font-size:13px;padding:4px 22px;border-radius:3px}
/* hero */
.hero-photo{left:0;top:0;width:1200px;height:820px;background:linear-gradient(160deg,#8a9bb0 0%,#c9b79a 45%,#e08a3a 70%,#5b4a3c 100%)}
.sidebar{position:absolute;left:0;top:0;width:110px;height:820px;background:rgba(255,255,255,.92)}
.sidebar .cap{background:var(--blue);color:#fff;font-size:14px;text-align:center;padding:10px 0 6px;line-height:1.3}
.sidebar .cap small{display:block;font-size:9px}
.sidebar li{list-style:none;font-size:14px;padding:10px 0 10px 14px;border-bottom:1px solid #dde3ea}
.topnav{position:absolute;left:180px;top:20px;display:flex;gap:34px;color:#fff;font-size:14px;opacity:.85}
.logo{position:absolute;left:490px;top:14px;width:220px;height:92px;background:#fff;border-radius:4px;display:flex;align-items:center;justify-content:center;gap:10px}
.logo .dot{width:16px;height:16px;border-radius:50%;background:var(--teal)}
.logo .name{font-size:26px;font-weight:700;color:var(--navy)}
.tel{position:absolute;right:12px;top:6px;background:#fff;padding:2px 14px;display:flex;align-items:center;gap:8px;font-size:26px;font-weight:700;color:var(--navy)}
.tagline{left:0;top:820px;height:110px;background:linear-gradient(90deg,rgba(255,255,255,0),#fff 30%);text-align:center;padding-top:14px;padding-left:260px;font-family:"Noto Serif JP",serif;font-weight:700;font-size:30px;line-height:1.35;color:var(--navy)}
.tagline .hl{color:var(--red)}
.intro{left:0;top:950px;text-align:center;font-size:17px;line-height:2;padding-left:240px}
.intro .hl{color:var(--red)}
/* voice */
.voice-grid{left:80px;top:1210px;width:440px;height:230px;display:grid;grid-template-columns:1fr 1fr;gap:6px}
.voice-grid div{background:linear-gradient(135deg,#dfe5ec,#9aa7b6)}
.voice-grid div:first-child{background:linear-gradient(135deg,#2a4a6e,#8aa0b8)}
.voice-video{left:540px;top:1210px;width:590px;height:230px;background:linear-gradient(120deg,#e7eaee,#b7c0ca 60%,#f3f4f6)}
.dots{left:0;top:1456px;display:flex;justify-content:center;gap:10px}
.dots i{width:10px;height:10px;border-radius:50%;background:#c5ccd4}
.dots i:first-child{background:var(--blue)}
/* service */
.svc-box{position:absolute;background:rgba(255,255,255,.94);padding:18px 26px;font-size:14px;line-height:1.7}
.svc-box h3{display:inline-block;background:var(--teal);color:#fff;font-size:18px;padding:4px 16px;margin-bottom:10px;border-radius:0 14px 0 0}
.svc-box .btn{margin-top:8px}
/* blog */
.blog-bg{left:0;top:2650px;height:820px;background:var(--mist)}
.post{position:absolute;left:50px;width:600px;height:150px;border-bottom:1px solid #cdd6df;display:flex;gap:20px;align-items:flex-start;padding-top:12px}
.post .thumb{width:170px;height:110px;flex:none}
.post .date{font-size:12px;color:var(--muted)}
.post .title{font-size:16px;font-weight:500}
.post .more{position:absolute;right:6px;bottom:12px;font-size:12px;color:var(--blue)}
.feed{left:690px;top:2740px;width:460px;height:690px;background:#fff;border:1px solid #cdd6df;padding:16px;font-size:12px}
.feed .head{display:flex;gap:12px;align-items:center;border-bottom:1px solid #e3e8ee;padding-bottom:12px}
.feed .sq{width:56px;height:56px;background:var(--teal);color:#fff;font-weight:700;display:flex;align-items:center;justify-content:center;font-size:13px}
.feed .line{height:8px;background:#e3e8ee;margin:8px 0;border-radius:2px}
/* recruit */
.rec-photo{left:0;top:3560px;width:1200px;height:400px;background:linear-gradient(180deg,#b9c6d4,#6d7f94 60%,#3e4b5c)}
.rec-box{left:370px;top:3650px;width:460px;height:200px;background:rgba(255,255,255,.88);text-align:center;padding-top:24px;font-family:"Noto Serif JP",serif;font-weight:700;color:var(--navy);font-size:34px;line-height:1.4}
.rec-box .sub{font-size:22px}
.rec-box .btn{font-family:"Noto Sans JP",sans-serif;font-weight:400;margin-top:14px;font-size:14px}
/* message */
.msg{left:50px;top:4110px;width:700px}
.msg .q{display:inline-block;background:var(--navy);color:#fff;font-family:"Noto Serif JP",serif;font-weight:700;font-size:26px;padding:4px 16px}
.msg .q2{font-family:"Noto Serif JP",serif;font-weight:700;font-size:26px;color:var(--navy);margin:8px 0 16px}
.msg p{font-size:14px;line-height:1.85;margin-bottom:12px}
.msg-photo{left:790px;top:4120px;width:340px;height:420px;background:linear-gradient(180deg,#f2f4f7,#c9d1db 55%,#2c3a4f)}
/* company */
.company{left:50px;top:4680px;width:260px;font-size:14px;line-height:1.7}
.company .tel2{font-size:24px;font-weight:700;color:var(--navy);display:flex;align-items:center;gap:6px;margin-top:8px}
.map{left:340px;top:4680px;width:810px;height:300px;background:linear-gradient(135deg,#eef0ec,#dfe4dc 50%,#e9e6dc)}
/* footer */
.footer{left:0;top:5000px;height:340px;background:var(--navy);color:#fff;display:flex;gap:70px;padding:40px 0 0 60px;font-size:14px}
.footer h4{font-size:15px;border-bottom:1px solid rgba(255,255,255,.4);padding-bottom:6px;margin-bottom:8px;width:160px}
.footer li{list-style:none;font-size:13px;opacity:.85}
.totop{position:absolute;right:24px;top:5250px;width:44px;height:44px;background:#fff;color:var(--navy);font-size:11px;text-align:center;line-height:44px;border-radius:2px}
.copy{left:0;top:5340px;height:60px;background:var(--navy-deep);color:#cfd8e3;font-size:12px;text-align:center;line-height:60px}
</style>
</head>
<body>

<header>
  <div class="ph hero-photo" role="img" aria-label="ハロウィンのかぼちゃ装飾がある会場でセミナー講師が話している写真"></div>
  <nav class="sidebar">
    <div class="cap">会社概要<small>Company</small></div>
    <ul><li>▸ 概要</li><li>▸ 社長挨拶</li></ul>
  </nav>
  <div class="topnav"><span>サービス</span><span>クライアントの声</span><span>歯科塾</span><span>Blog</span></div>
  <div class="logo"><span class="dot"></span><span class="name">Meadowpath</span></div>
  <div class="tel">
    <svg width="24" height="24" viewBox="0 0 24 24"><rect width="24" height="24" fill="#1d3557"/><path d="M7 5l3 3-2 2c1 2 3 4 5 5l2-2 3 3-2 3c-5 0-11-6-11-11z" fill="#fff"/></svg>
    03-4820-7316
  </div>
</header>

<section>
  <div class="block tagline">クライアントの <span class="hl">“こうしたい”</span> に<br><span class="hl">“そこまでやるか”</span> でカタチにする。</div>
  <div class="block intro">0から1を生み出せる、スキルや想いをもった私たち自身が、<br>同じような想い、高いスキルを持った個人や組織と繋がることによって<br><span class="hl">世の中に価値あるものを生み出していく。</span></div>
</section>

<section>
  <div class="sec-head" style="top:1140px"><span class="en">Voice</span><span class="ja">— クライアントの声 —</span></div>
  <div class="ph voice-grid" role="img" aria-label="クライアントの声の動画サムネイル4件"><div></div><div></div><div></div><div></div></div>
  <div class="ph voice-video" role="img" aria-label="クライアントへのインタビュー動画"></div>
  <svg class="ph" style="left:800px;top:1290px" width="70" height="70" viewBox="0 0 70 70"><circle cx="35" cy="35" r="34" fill="rgba(255,255,255,.85)"/><path d="M28 22l20 13-20 13z" fill="#2b5f9e"/></svg>
  <div class="block dots"><i></i><i></i><i></i></div>
</section>

<section>
  <div class="sec-head" style="top:1620px"><span class="en">Service</span><span class="ja">— サービス —</span></div>
  <div class="ph" style="left:0;top:1690px;width:1200px;height:260px;background:linear-gradient(90deg,#eef1f4,#c7ced7)" role="img" aria-label="タブレットを操作する手元の写真"></div>
  <div class="svc-box" style="left:40px;top:1700px;width:520px">
    <h3>歯科医院専門コンサルティング</h3>
    <div>医院の規模・状況・人員体制・地域性を考慮しながら、目標とするゴールに向かってオーダーメイドでプログラムを構築します。</div>
    <span class="btn">詳しく ›</span>
  </div>
  <div class="ph" style="left:0;top:1960px;width:1200px;height:280px;background:linear-gradient(90deg,#3c4047,#a6adb6 60%,#dfe3e8)" role="img" aria-label="キーボードを打つ手元の写真"></div>
  <div class="svc-box" style="left:640px;top:1990px;width:520px">
    <h3>ホームページ作成</h3>
    <div>歯科医院運営を軸に、ホームページが不可欠であることは言うまでもありません。ホームページを作っても結果が出ない歯科医院が多い中、結果を出すホームページを作成します。</div>
    <span class="btn">詳しく ›</span>
  </div>
  <div class="ph" style="left:0;top:2250px;width:1200px;height:360px;background:linear-gradient(135deg,#6a5a4c,#b08a6a 50%,#4a4e58)" role="img" aria-label="勉強会で参加者が話し合う写真"></div>
  <div class="svc-box" style="left:40px;top:2290px;width:520px">
    <h3>歯科塾（歯科医大のコミュニティ）</h3>
    <div>自分ひとりで考えていても、自分の医院だけではなかなか解決できないこともあります。志の高いメンバーが集まることで、課題を共有し、知恵を出し合うことで前向きな解決策が見えてきます。</div>
    <span class="btn">詳しく ›</span>
  </div>
</section>

<section>
  <div class="block blog-bg"></div>
  <div class="sec-head" style="top:2660px"><span class="en">Blog</span><span class="ja">— ブログ —</span></div>
  <div class="post" style="top:2740px"><div class="thumb" style="background:linear-gradient(135deg,#2f4d72,#9fb3c8)" role="img" aria-label="セミナー風景の写真"></div><div><div class="date">2017.07.25</div><div class="title">あらゆる課題を解決してきた歯科医院の実績事例</div></div><span class="more">more ›</span></div>
  <div class="post" style="top:2900px"><div class="thumb" style="background:linear-gradient(135deg,#c8d6e6,#6f8db0)" role="img" aria-label="ビジネスの図解イメージ"></div><div><div class="date">2017.06.15</div><div class="title">新営業者の見える化による着実な採用支援</div></div><span class="more">more ›</span></div>
  <div class="post" style="top:3060px"><div class="thumb" style="background:linear-gradient(135deg,#e6eef6,#7ea2c8)" role="img" aria-label="人の集まりのイメージ"></div><div><div class="date">2017.06.06</div><div class="title">再現性のある人財開発改善ノウハウ</div></div><span class="more">more ›</span></div>
  <div class="post" style="top:3220px"><div class="thumb" style="background:linear-gradient(135deg,#5b7ea6,#d8e3ee)" role="img" aria-label="ネットワークのイメージ"></div><div><div class="date">2017.05.21</div><div class="title">幅広いニーズに対応するためのネットワーク</div></div><span class="more">more ›</span></div>
  <div class="ph feed">
    <div class="head"><div class="sq">歯科塾</div><div><b style="font-size:15px">歯科塾</b><br>いいね！ 128件</div></div>
    <div style="margin-top:12px">歯科塾より最新のお知らせです。</div>
    <div class="line" style="width:90%"></div><div class="line" style="width:75%"></div>
    <div style="margin-top:10px">2017年8月10日 12:00〜18:00 勉強会開催のご案内</div>
    <div class="line" style="width:85%"></div><div class="line" style="width:60%"></div>
    <div style="height:260px;margin-top:16px;background:linear-gradient(180deg,#f4f7fa,#d6e2ec)" role="img" aria-label="歯科塾の告知画像"></div>
    <div style="margin-top:14px;font-weight:700">歯科塾 第6期 参加メンバー募集のお知らせ</div>
    <div class="line" style="width:80%"></div><div class="line" style="width:70%"></div>
  </div>
</section>

<section>
  <div class="sec-head" style="top:3490px"><span class="en">Recruit</span><span class="ja">— リクルート —</span></div>
  <div class="ph rec-photo" role="img" aria-label="オフィス街を歩くビジネスパーソンの写真"></div>
  <div class="ph rec-box">一緒に翔ぼう！<div class="sub">あなたが動けば、世界も動き出す。</div><span class="btn">採用ページはこちら ›</span></div>
</section>

<section>
  <div class="sec-head" style="top:4030px"><span class="en">Message</span><span class="ja">— メッセージ —</span></div>
  <div class="ph msg">
    <div class="q">「困っている人を助けたい」</div>
    <div class="q2">そんな想いでメドウパスは始まった。</div>
    <p>そのような私達のクライアントのあらゆるニーズに的確に応えるようになり、当社では、創業以来、歯科医院専門の経営コンサルティング・マーケティング会社として歯科医院様の経営改善・経営支援のサポートを続けてまいりました。</p>
    <p>クライアントにとって重要度が高い課題は何なのかをコンサルタントの視点、患者様の視点から総合的に判断して解決策をご提案しています。これは、歯科医院専門のコンサルタントが創設した会社だからこそ出来ることです。</p>
    <p>医院の経営をよりよくしたい経営者の皆様に最適なコンサルティングをご提供し、歯科医院経営を成功に導くため、私たちはこれからも挑戦を続けてまいります。</p>
  </div>
  <div class="ph msg-photo" role="img" aria-label="スーツ姿の代表者がタブレットを持って立つ写真"></div>
</section>

<section>
  <div class="ph company">
    <div>株式会社メドウパス<br>Meadowpath Co.,Ltd</div>
    <div style="margin-top:12px">〒160-0099<br>東京都新宿区架空町3-8-2<br>メドウパスビル5階</div>
    <span class="btn" style="margin-top:12px">お問い合わせ ›</span>
    <div class="tel2"><svg width="22" height="22" viewBox="0 0 24 24"><rect width="24" height="24" fill="#1d3557"/><path d="M7 5l3 3-2 2c1 2 3 4 5 5l2-2 3 3-2 3c-5 0-11-6-11-11z" fill="#fff"/></svg>03-4820-7316</div>
  </div>
  <div class="ph map" role="img" aria-label="本社所在地周辺の地図"></div>
  <svg class="ph" style="left:730px;top:4790px" width="30" height="42" viewBox="0 0 30 42"><path d="M15 0C7 0 0 6 0 15c0 11 15 27 15 27s15-16 15-27C30 6 23 0 15 0z" fill="#e0322f"/><circle cx="15" cy="15" r="6" fill="#fff"/></svg>
</section>

<footer>
  <div class="block footer">
    <div><h4>会社概要</h4><ul><li>▸ 概要</li><li>▸ 社長挨拶</li></ul></div>
    <div><h4>サービス</h4><ul><li>▸ コンサルティング</li><li>▸ HP</li><li>▸ 塾</li></ul></div>
    <div><h4>クライアントの声</h4><ul><li>▸ ダミーテキスト</li><li>▸ ダミーテキスト</li><li>▸ ダミーテキスト</li></ul></div>
    <div><h4>歯科塾</h4><ul><li>▸ ダミーテキスト</li><li>▸ ダミーテキスト</li><li>▸ ダミーテキスト</li></ul></div>
    <div><h4>Blog</h4><ul><li>▸ ダミーテキスト</li><li>▸ ダミーテキスト</li><li>▸ ダミーテキスト</li></ul></div>
  </div>
  <div class="totop">TOP ▲</div>
  <div class="block copy">Copyright © Meadowpath Co.,Ltd All Right Reserved.</div>
</footer>

</body>
</html>
```